R&T Marketing / P.L.B. Sales Business Cards

I have 2 companies that are somewhat connected, yet sell to 2 different markets.

R&T Marketing www.ratendpx.example

We are a manufacturers representative company. We handle sales and marketing of Home Theater, Home Automation, Audio & Video products for the state of Florida. We work with Designers, Architects, Technology Consultants and Electronic Integrators to design, sell and install cutting edge technology in new and existing homes, condos and commercial spaces.

P.L.B. Sales www.plbpx.example

We are a manufacturers representative company. We handle sales and marketing of automotive Audio, Electronics, Security, Navigation and Entertainment products for the state of Florida. We work with 12-volt retailers, installers and automobile customizers to design, sell, merchandise, fabricate and install cutting edge technology in cars, boats, motor coaches, etc.

We have logo's that might still be relevant, but might need a little touching up. We need a new business card design and layout for each of the 2 companies. I would like them to have a family look, but still better speak to the customer base associated with the channel.

Target Market(s)

R&T Marketing -

Design, Engineering, Construction, Technology, elegant, tasteful.

P.L.B. Sales -

More cutting edge, industrial, youth, aggressive, fun, bold.

Requirements
Must have
• New business card layout for both companies.
Nice to have
• A family look, or relationship to the other company. Even if it's just a logo referencing the other company.

```html
<!DOCTYPE html>
<html lang="en">
<head>
<meta charset="utf-8">
<title>R&amp;T Marketing Business Cards</title>
<link rel="stylesheet" href="https://fonts.googleapis.com/css2?family=Mulish:wght@400;600;800&display=swap">
<style>
  :root {
    --canvas-bg: #e9ebee;
    --navy: #13386e;
    --navy-deep: #0f2f63;
    --blue: #1a6fb5;
    --blue-bright: #2a86cc;
    --card-white: #f7f8fa;
    --ink: #2b3f66;
    --ink-soft: #4a5670;
    --logo-ink: #3c4f78;
  }
  * { box-sizing: border-box; margin: 0; padding: 0; }
  html, body {
    width: 1200px; height: 800px; overflow: hidden;
    background: var(--canvas-bg);
    font-family: "Mulish", sans-serif;
  }
  .canvas {
    position: relative; width: 1200px; height: 800px;
  }
  .card {
    position: absolute;
    width: 520px; height: 297px;
    top: 252px;
    box-shadow: 0 6px 18px rgba(20, 30, 50, 0.18);
    overflow: hidden;
  }
  .card--front {
    left: 50px;
    background: linear-gradient(100deg, var(--navy-deep) 0%, var(--navy) 45%, var(--blue) 100%);
  }
  .front-glow {
    position: absolute; right: 0; bottom: 0;
    width: 340px; height: 190px;
    background: radial-gradient(ellipse at 80% 100%, rgba(58, 150, 220, 0.75) 0%, rgba(42, 134, 204, 0.35) 45%, rgba(42, 134, 204, 0) 75%);
  }
  .brand-name {
    position: absolute;
    font-family: "Mulish", sans-serif;
    font-weight: 600;
    letter-spacing: 1px;
    white-space: nowrap;
  }
  .card--front .brand-name {
    left: 48px; top: 118px;
    font-size: 36px;
    color: #ffffff;
  }
  .card--back {
    left: 630px;
    background: var(--card-white);
  }
  .card--back .brand-name {
    left: 36px; top: 120px;
    font-size: 28px;
    color: var(--logo-ink);
  }
  .back-band {
    position: absolute; bottom: 0; height: 20px;
  }
  .back-band--left { left: 0; width: 278px; background: var(--navy); }
  .back-band--right { left: 282px; right: 0; background: var(--blue-bright); }
  .contact {
    position: absolute; left: 300px; top: 50px;
    color: var(--ink);
  }
  .contact__name {
    font-weight: 800; font-size: 13.5px; letter-spacing: 0.6px;
    color: var(--navy);
  }
  .contact__title {
    font-size: 11px; color: var(--ink-soft); margin-top: 2px;
  }
  .contact__list {
    list-style: none; margin-top: 16px;
  }
  .contact__item {
    display: flex; align-items: center; gap: 7px;
    font-size: 11.5px; line-height: 15px; color: var(--ink-soft);
  }
  .contact__item svg { width: 11px; height: 11px; flex: none; }
  .contact__address {
    margin-top: 14px; font-size: 11.5px; line-height: 15px;
    color: var(--ink-soft); font-style: normal;
  }
</style>
</head>
<body>
<main class="canvas">
  <section class="card card--front" aria-label="Card front">
    <div class="front-glow" role="img" aria-label="Blue halftone dot pattern fading in from the lower right"></div>
    <div class="brand-name">R&amp;T Marketing</div>
  </section>

  <section class="card card--back" aria-label="Card back">
    <div class="brand-name">R&amp;T Marketing</div>

    <div class="contact">
      <div class="contact__name">DANIEL KORVATH</div>
      <div class="contact__title">Rep Principle</div>
      <ul class="contact__list">
        <li class="contact__item">
          <svg viewBox="0 0 12 12"><circle cx="6" cy="6" r="5.4" fill="none" stroke="#4a5670" stroke-width="0.9"/><rect x="4.2" y="2.8" width="3.6" height="6.4" rx="0.6" fill="none" stroke="#4a5670" stroke-width="0.9"/></svg>
          555-214-0198
        </li>
        <li class="contact__item">
          <svg viewBox="0 0 12 12"><circle cx="6" cy="6" r="5.4" fill="none" stroke="#4a5670" stroke-width="0.9"/><path d="M3.8 3.4c0.4-0.4 0.9-0.3 1.1 0.1l0.4 0.9c0.1 0.3 0 0.6-0.3 0.8 0.3 0.8 0.9 1.4 1.7 1.7 0.2-0.3 0.5-0.4 0.8-0.3l0.9 0.4c0.4 0.2 0.5 0.7 0.1 1.1-1.6 1.5-5.9-2.6-4.7-4.7z" fill="#4a5670"/></svg>
          800-555-0147
        </li>
        <li class="contact__item">
          <svg viewBox="0 0 12 12"><circle cx="6" cy="6" r="5.4" fill="none" stroke="#4a5670" stroke-width="0.9"/><rect x="3" y="4" width="6" height="4.2" fill="none" stroke="#4a5670" stroke-width="0.8"/><path d="M3 4l3 2.3 3-2.3" fill="none" stroke="#4a5670" stroke-width="0.8"/></svg>
          daniel@ratendpx.example
        </li>
        <li class="contact__item">
          <svg viewBox="0 0 12 12"><circle cx="6" cy="6" r="5.4" fill="none" stroke="#4a5670" stroke-width="0.9"/><ellipse cx="6" cy="6" rx="2.2" ry="5.4" fill="none" stroke="#4a5670" stroke-width="0.7"/><path d="M0.8 6h10.4" stroke="#4a5670" stroke-width="0.7"/></svg>
          www.ratendpx.example
        </li>
      </ul>
      <address class="contact__address">
        4120 Harbor View Lane<br>
        Tampa, FL 33602
      </address>
    </div>

    <div class="back-band back-band--left"></div>
    <div class="back-band back-band--right"></div>
  </section>
</main>
</body>
</html>
```